Business Card Bright Willow Path
Professional
Marla Quennby, CPCC, MA, DipM
Founder
HTMA Administration Office
PO Box 27381
Birmingham
B47 3KT
info@brightwillowpath.co.uk
brightwillowpath.co.uk
Please use both variations of the logo while submitting design.
Business cards to look modern, fresh, feminine, in alignment with logo branding.
Small print to say: a division of The Harbor Trust For Mentoring Ambition
Colour scheme, images and writting to co ordinate with logo.
I do not want the address on the business cards
The market for these cards is proffessional women hence a modern, proffessional yet not too corporate and not "woo woo".
I do not want the address on the business cards.

```html
<!DOCTYPE html>
<html lang="en">
<head>
<meta charset="utf-8">
<title>Bright Willow Path – Business Card</title>
<link rel="stylesheet" href="https://fonts.googleapis.com/css2?family=Cinzel:wght@400;600&family=Cormorant+Garamond:ital,wght@0,500;0,600;1,500&display=swap">
<style>
  :root {
    --rose: #c94b53;
    --rose-deep: #b23a43;
    --rose-light: #db6a70;
    --paper: #ffffff;
    --ink: #4a4a4a;
    --ground: #e9e7e6;
  }
  * { margin: 0; padding: 0; box-sizing: border-box; }
  html, body { width: 1200px; height: 864px; overflow: hidden; }
  body { background: var(--ground); position: relative; font-family: "Cormorant Garamond", serif; }

  .card {
    position: absolute;
    top: 262px;
    width: 540px;
    height: 340px;
    border-radius: 20px;
    overflow: hidden;
    box-shadow: 0 10px 28px rgba(0,0,0,.18);
  }

  /* Back of card */
  .card-back {
    left: 40px;
    background: linear-gradient(160deg, var(--rose-light) 0%, var(--rose) 45%, var(--rose-deep) 100%);
    color: var(--paper);
  }
  .card-back .brand {
    position: absolute;
    left: 0; right: 0; top: 130px;
    display: flex; flex-direction: column; align-items: center; gap: 14px;
  }
  .brand-dot { width: 34px; height: 34px; border-radius: 50%; background: var(--paper); }
  .card-back .brand-name {
    font-family: "Cinzel", serif; font-weight: 400; font-size: 22px; letter-spacing: 3px;
  }
  .division-note {
    position: absolute; right: 30px; bottom: 26px;
    font-family: "Cinzel", serif; font-size: 10.5px; letter-spacing: .6px;
  }

  /* Front of card */
  .card-front { left: 620px; background: var(--paper); }
  .swoosh { position: absolute; left: 0; top: 0; width: 540px; height: 340px; }

  .identity {
    position: absolute; left: 26px; top: 166px; width: 290px;
    display: flex; flex-direction: column; align-items: center;
    z-index: 1;
  }
  .identity .brand-dot { width: 30px; height: 30px; background: var(--rose); margin-bottom: 10px; }
  .identity .brand-name {
    font-family: "Cinzel", serif; font-weight: 400; font-size: 21px; letter-spacing: 1.5px; color: var(--rose);
    white-space: nowrap;
  }
  .tagline {
    font-style: italic; font-size: 11px; color: var(--rose); margin-top: 2px; white-space: nowrap;
  }

  .contact {
    position: absolute; left: 296px; top: 50px;
    font-family: "Cinzel", serif; color: var(--ink);
    z-index: 1;
  }
  .contact .person { font-size: 12px; font-weight: 600; letter-spacing: .5px; color: var(--rose); line-height: 1.5; }
  .contact .role { font-size: 10.5px; letter-spacing: .5px; margin-bottom: 10px; }
  .contact ul { list-style: none; }
  .contact li {
    display: flex; align-items: center; gap: 7px;
    font-size: 9.5px; letter-spacing: .4px; line-height: 1; margin-bottom: 6px;
    white-space: nowrap;
  }
  .icon { width: 12px; height: 12px; flex: none; }
</style>
</head>
<body>

  <section class="card card-back">
    <div class="brand">
      <span class="brand-dot"></span>
      <span class="brand-name">BRIGHT WILLOW PATH</span>
    </div>
    <p class="division-note">A Division of The Harbor Trust For Mentoring Ambition</p>
  </section>

  <section class="card card-front">
    <svg class="swoosh" viewBox="0 0 540 340" aria-hidden="true">
      <path d="M0 300 C 200 308, 400 268, 540 136 L540 148 C 400 282, 200 320, 0 312 Z" fill="var(--rose-light)"/>
      <path d="M0 322 C 200 330, 400 290, 540 160 L540 340 L0 340 Z" fill="var(--rose)"/>
      <path d="M0 334 C 200 342, 420 306, 540 196 L540 340 L0 340 Z" fill="var(--rose-deep)"/>
    </svg>

    <div class="identity">
      <span class="brand-dot"></span>
      <span class="brand-name">BRIGHT WILLOW PATH</span>
      <span class="tagline">nurturing your spirit, purpose, voice and growth</span>
    </div>

    <div class="contact">
      <p class="person">Marla Quennby, CPCC,</p>
      <p class="role">MA, DipM | Founder</p>
      <ul>
        <li>
          <svg class="icon" viewBox="0 0 12 12"><circle cx="6" cy="6" r="6" fill="var(--rose)"/><path d="M4 3.2l1 1.4-.6.7a4 4 0 0 0 2.3 2.3l.7-.6 1.4 1-.6 1C6.2 9 3 5.8 3.1 3.8z" fill="#fff"/></svg>
          +44 121 555 0142
        </li>
        <li>
          <svg class="icon" viewBox="0 0 12 12"><circle cx="6" cy="6" r="6" fill="var(--rose)"/><rect x="4.2" y="2.6" width="3.6" height="6.8" rx=".6" fill="#fff"/></svg>
          +44 7700 900 318
        </li>
        <li>
          <svg class="icon" viewBox="0 0 12 12"><circle cx="6" cy="6" r="6" fill="var(--rose)"/><rect x="3" y="4" width="6" height="4.2" fill="#fff"/><path d="M3 4l3 2.3L9 4" stroke="var(--rose)" stroke-width=".7" fill="none"/></svg>
          info@brightwillowpath.co.uk
        </li>
        <li>
          <svg class="icon" viewBox="0 0 12 12"><circle cx="6" cy="6" r="6" fill="var(--rose)"/><circle cx="6" cy="6" r="3" fill="none" stroke="#fff" stroke-width=".8"/><path d="M3 6h6M6 3v6" stroke="#fff" stroke-width=".6"/></svg>
          www.brightwillowpath.co.uk
        </li>
      </ul>
    </div>
  </section>

</body>
</html>
```